Business card for Bright Keystone

Front (space for each) - Name, title, qualifications, mobile number, email address, website, name/logo,
Back - Business name/logo and slogan "your dream is our vision" underneath,
in small writing underneath need ABN number, CRN number, ACL number
Target Market(s)
First Home Buyers
Industry/Entity Type
Finance
Contact Information for Business Card
Requirements
Must have
- Front (space for each) - Name, title, qualifications, mobile number, email address, website, name/logo,

```html
<!DOCTYPE html>
<html lang="en">
<head>
<meta charset="utf-8">
<title>Bright Keystone — Business Card</title>
<link href="https://fonts.googleapis.com/css2?family=Jost:wght@400;500;600&family=Montserrat:wght@400;600&display=swap" rel="stylesheet">
<style>
  :root {
    --backdrop: #2b2b2d;
    --card-black: #050505;
    --card-white: #ffffff;
    --teal: #12a99f;
    --green: #86c540;
    --coral: #f06a4f;
    --ink: #1d1d1f;
    --muted: #cfcfcf;
  }
  * { box-sizing: border-box; margin: 0; padding: 0; }
  html, body {
    width: 1200px; height: 1000px; overflow: hidden;
    background: var(--backdrop);
  }
  .canvas { position: relative; width: 1200px; height: 1000px; }
  .card {
    position: absolute; left: 250px; width: 700px; height: 400px;
    border-radius: 18px; overflow: hidden;
  }
  /* Back of card */
  .card--back {
    top: 70px; background: var(--card-black);
    display: flex; flex-direction: column; align-items: center; justify-content: center;
    font-family: "Jost", sans-serif; color: #fff;
  }
  .brand { display: flex; align-items: center; gap: 16px; }
  .brand__dot {
    width: 22px; height: 22px; border-radius: 50%; background: var(--coral); flex: none;
  }
  .brand__name {
    font-family: "Jost", sans-serif; font-weight: 600;
    font-size: 46px; letter-spacing: 4px; text-transform: uppercase; line-height: 1;
  }
  .card--back .brand__name { color: #fff; }
  .slogan {
    margin-top: 26px; font-size: 24px; font-weight: 500;
    letter-spacing: 3px; text-transform: uppercase;
  }
  .registrations {
    margin-top: 22px; display: flex; gap: 26px;
    font-size: 12px; letter-spacing: 1.5px; text-transform: uppercase; color: var(--muted);
  }
  .card__band {
    position: absolute; left: 0; right: 0; bottom: 0; height: 8px; display: flex;
  }
  .card__band span { flex: 1; }
  .card__band .band-teal { background: var(--teal); }
  .card__band .band-green { background: var(--green); }

  /* Front of card */
  .card--front {
    top: 540px; background: var(--card-white);
    font-family: "Jost", sans-serif; color: var(--ink);
  }
  .person { position: absolute; left: 50px; top: 90px; width: 360px; }
  .person__name {
    font-size: 40px; font-weight: 500; color: var(--teal);
    letter-spacing: 3px; text-transform: uppercase; line-height: 1;
  }
  .person__title {
    margin-top: 10px; font-size: 15px; letter-spacing: 2px; text-transform: uppercase;
  }
  .person__rule { margin-top: 12px; height: 2px; background: var(--green); width: 340px; }
  .contact {
    list-style: none; margin-top: 22px;
    font-family: "Montserrat", sans-serif; font-size: 15px;
  }
  .contact li { display: flex; align-items: center; gap: 14px; margin-bottom: 14px; }
  .contact .contact__phone { font-weight: 600; }
  .contact svg { width: 24px; height: 24px; flex: none; }
  .card--front .brand {
    position: absolute; right: 50px; top: 110px;
    flex-direction: column; align-items: flex-end; gap: 18px;
  }
  .card--front .brand__name {
    font-size: 40px; color: var(--teal); letter-spacing: 3px; text-align: right; line-height: 1.1;
  }
  .brand__line { display: block; }
  .card--front .brand__dot { width: 30px; height: 30px; margin-right: 20px; }
</style>
</head>
<body>
<main class="canvas">
  <section class="card card--back" aria-label="Card back">
    <div class="brand">
      <span class="brand__dot"></span>
      <span class="brand__name">Bright Keystone</span>
    </div>
    <p class="slogan">Your dream is our vision</p>
    <p class="registrations">
      <span>ABN Number: BK240731</span>
      <span>CRN Number: BK240731</span>
      <span>ACL Number: BK240731</span>
    </p>
    <div class="card__band"><span class="band-teal"></span><span class="band-green"></span></div>
  </section>

  <section class="card card--front" aria-label="Card front">
    <div class="person">
      <h1 class="person__name">Daniel Hart</h1>
      <p class="person__title">Managing Director, MD</p>
      <div class="person__rule"></div>
      <ul class="contact">
        <li class="contact__phone">
          <svg viewBox="0 0 24 24" aria-hidden="true"><path fill="#12a99f" d="M6.6 10.8a15 15 0 0 0 6.6 6.6l2.2-2.2a1 1 0 0 1 1-.25 11.4 11.4 0 0 0 3.6.57 1 1 0 0 1 1 1V20a1 1 0 0 1-1 1A17 17 0 0 1 3 4a1 1 0 0 1 1-1h3.5a1 1 0 0 1 1 1c0 1.25.2 2.45.57 3.57a1 1 0 0 1-.25 1z"/></svg>
          (208) 555-0147
        </li>
        <li>
          <svg viewBox="0 0 24 24" aria-hidden="true"><rect x="2.5" y="5" width="19" height="14" rx="1" fill="none" stroke="#12a99f" stroke-width="1.6"/><path d="M3 6l9 7 9-7" fill="none" stroke="#12a99f" stroke-width="1.6"/></svg>
          danielhart@brightkeystone.com
        </li>
        <li>
          <svg viewBox="0 0 24 24" aria-hidden="true"><circle cx="12" cy="12" r="9.5" fill="none" stroke="#12a99f" stroke-width="1.6"/><ellipse cx="12" cy="12" rx="4.5" ry="9.5" fill="none" stroke="#12a99f" stroke-width="1.4"/><path d="M2.5 12h19M4 7.5h16M4 16.5h16" stroke="#12a99f" stroke-width="1.2"/></svg>
          www.brightkeystone.com
        </li>
      </ul>
    </div>
    <div class="brand">
      <span class="brand__name"><span class="brand__line">Bright</span><span class="brand__line">Keystone</span></span>
      <span class="brand__dot"></span>
    </div>
  </section>
</main>
</body>
</html>
```